Noche de Salsa

We need a poster to promote a party. It is a salsa night at La Tortuga, a fun night out to dance, be with friends and have a few drinks. It is an informal occasion. The drinks will not be expensive and the snack will be typical mexican food.
La Tortuga is a campus for 8 local non-profit organizations but it also has high quality event venues and outdoor areas.
We would like a file for print (11x17") and a digital file for social media.
Enclosed:
- File with poster contents in spanish.
- La Tortuga logo
- Picture of palm trees at La Tortuga (you don't have to include this if another graphic fits best.
- Pic of the outside of the restaurant, where the dancing will take place. The restaurante is right in fron of the beach. THIS PICTURE DOES NOT NECESSARILY NEEDS TO BE PART OF THE POSTER.
- La Tortuga Fact Sheet for context.
Target Market(s)
Men and women from 25 to 50 years old.
American and mexican citizens.
Industry/Entity Type
Non-Profit
Colors
Designer to choose colors to be used in the design.
Look and feel
Each slider illustrates characteristics of the customer's brand and the style your logo design should communicate.

```html
<!DOCTYPE html>
<html lang="es">
<head>
<meta charset="utf-8">
<title>Noche de Salsa · La Tortuga</title>
<link rel="stylesheet" href="https://fonts.googleapis.com/css2?family=Great+Vibes&family=Raleway:wght@400;500&display=swap">
<style>
  :root {
    --backdrop: #d9d4cc;
    --night: #050505;
    --salsa-red: #e0313c;
    --leaf-green: #4d5e1e;
    --paper: #ffffff;
    --ink: #3d3d3d;
    --light-text: #f2f2f2;
  }
  * { margin: 0; padding: 0; box-sizing: border-box; }
  html, body { width: 890px; height: 1200px; overflow: hidden; }
  body { background: var(--backdrop); position: relative; font-family: "Raleway", Arial, sans-serif; }

  .poster {
    position: absolute; left: 133px; top: 118px;
    width: 624px; height: 964px;
    background: var(--night); overflow: hidden;
    box-shadow: 0 6px 18px rgba(0,0,0,.35);
  }
  .poster__bands { position: absolute; inset: 0; }

  .poster__photo {
    position: absolute; left: 97px; top: 22px; width: 490px; height: 560px;
    background: radial-gradient(ellipse at 62% 52%, #a3121c 0%, #5a0a10 28%, #1f1a1a 55%, rgba(5,5,5,0) 78%);
  }

  .title { position: absolute; color: var(--paper); font-family: "Great Vibes", cursive; line-height: 1; }
  .title--noche { left: 140px; top: 330px; font-size: 118px; }
  .title--de { left: 325px; top: 440px; font-size: 96px; }
  .title--salsa { left: 128px; top: 470px; font-size: 118px; }

  .details { position: absolute; left: 357px; top: 538px; font-size: 14.5px; line-height: 20px; color: var(--light-text); }
  .details__label { color: var(--salsa-red); }
  .details__gap { margin-top: 4px; }

  .venue { position: absolute; left: 357px; top: 752px; color: var(--ink); font-size: 17px; line-height: 22px; }
  .venue__line--lead { margin-left: -1px; }
  .venue__note { font-size: 7.5px; line-height: 10px; margin-bottom: 3px; }
  .venue__contact { margin-top: 8px; }

  .brand { position: absolute; left: 68px; top: 830px; display: flex; align-items: center; gap: 12px; }
  .brand__dot { width: 22px; height: 22px; border-radius: 50%; background: var(--leaf-green); }
  .brand__name { font-size: 40px; font-weight: 500; color: var(--ink); letter-spacing: .5px; }
</style>
</head>
<body>
  <main class="poster">
    <svg class="poster__bands" width="624" height="964" viewBox="0 0 624 964" aria-hidden="true">
      <path d="M0,738 Q320,610 624,722 L624,964 L0,964 Z" fill="var(--salsa-red)"/>
      <path d="M0,742 Q300,650 624,748 L624,964 L0,964 Z" fill="var(--leaf-green)"/>
      <path d="M0,768 Q330,655 624,752 L624,964 L0,964 Z" fill="var(--paper)"/>
    </svg>

    <div class="poster__photo" role="img" aria-label="Pareja bailando salsa: él de negro, ella con vestido rojo en movimiento, sobre fondo negro"></div>

    <h1 class="title-group">
      <span class="title title--noche">noche</span>
      <span class="title title--de">de</span>
      <span class="title title--salsa">salsa</span>
    </h1>

    <section class="details">
      <p class="details__label">Entrada:</p>
      <p>$100 pesos</p>
      <p>Incluye 1 bebida.</p>
      <p class="details__label details__gap">Viernes</p>
      <p>14 de noviembre 2014</p>
    </section>

    <div class="brand">
      <span class="brand__dot"></span>
      <span class="brand__name">la tortuga</span>
    </div>

    <address class="venue" style="font-style:normal">
      <p class="venue__line--lead">Acceso Costero #1480</p>
      <p class="venue__note">(al final de la calle Marina, junto al viejo muelle)</p>
      <p>Col. Las Palmas</p>
      <p>C.P. 23410</p>
      <p>Bahía Serena, B.C.S.</p>
      <div class="venue__contact">
        <p>Más informes al</p>
        <p>555-0147</p>
        <p>info@latortuga.org</p>
      </div>
    </address>
  </main>
</body>
</html>
```